VerdaTurf - 11" x 4" Door Hanger, full color both sides

We need a door hanger designed, 11" x 4", full color both sides, We are a lawn care company that provides lawn mowing, and other services to clients. This door hanger will be place on the 9 neighbors of our current clients. The ad needs to state that we provided lawn service to one of their neighbors today, and that we are in their neighborhood each week on that day. The door hanger will have 4 printings, substituting the day of Tuesday, Wednesday, Thursday, and Friday. All the art work and text will remain the same except the day of the week. For information about VerdaTurf, please visit our website www.verdaturf-example.net. The main emphasis of the message should be that we are their every week on that day, and the benefits to them of using our service (ie. quality time with their family, golf, sports, resting, etc., instead of mowing the lawn). At the bottom of the door hanger will be a coupon offering their tenth (10th) lawn service free, which is the same as a 10% discount.

I have uploaded a template files for the front and back of an 11 x 4 door hanger, The templates are pdf, jpeg, or eps files. The final product can be a pdf, jpeg, or eps file.

Target Market(s)

Neighbors of our existing clients

Industry/Entity Type

Lawn Care

Font styles to use
Serif

Requirements
Must have
• Professional design and art, Short conversational message that relays the following thoughts:
• 1. We mowed your neighbor's lawn today!
• 2. We are in your neighborhood every Tuesday!
• 3. Our lawn service is guaranteed.
• 4. Call to action - Call us today! 512-748-3091
• 5. Of course our contact info, name, phone number, website address.
• 6. Coupon at bottom for "10th lawn service Free!"
Nice to have
• Art work from our website is fine to use, That carries our theme throughout our campaign.
Should not have
• Very wordy. This is basically a billboard, Have very few seconds to grab their attention.

```html
<!DOCTYPE html>
<html lang="en">
<head>
<meta charset="utf-8">
<title>VerdaTurf Door Hanger</title>
<link href="https://fonts.googleapis.com/css2?family=Montserrat:wght@300;400;500;600;700&family=Oswald:wght@500&display=swap" rel="stylesheet">
<style>
  :root{
    --bg:#1d1d1d;
    --red:#ee4747;
    --red-deep:#d93a3a;
    --green:#8dc63f;
    --green-deep:#6fae2a;
    --ink:#222222;
    --white:#ffffff;
    --mist:#e9e9e9;
    --sky:#3a8fd8;
    --turf:#4aa82a;
  }
  html,body{margin:0;padding:0;width:1200px;height:1200px;overflow:hidden;background:var(--bg);}
  .canvas{position:relative;width:1200px;height:1200px;}
  .hanger{position:absolute;top:130px;width:393px;height:941px;box-shadow:0 10px 30px rgba(0,0,0,.5);}
  .hanger--front{left:163px;}
  .hanger--back{left:645px;}
  .hanger svg{display:block;width:100%;height:100%;}
  .t-head{font-family:'Montserrat',sans-serif;font-weight:600;}
  .t-brand{font-family:'Montserrat',sans-serif;font-weight:300;letter-spacing:1px;}
  .t-body{font-family:'Montserrat',sans-serif;font-weight:400;}
  .t-bold{font-family:'Montserrat',sans-serif;font-weight:700;}
  .t-coupon{font-family:'Oswald',sans-serif;font-weight:500;}
</style>
</head>
<body>
<div class="canvas">

  <!-- Front side -->
  <div class="hanger hanger--front">
    <svg viewBox="0 0 458 1098" xmlns="http://www.w3.org/2000/svg">
      <defs>
        <linearGradient id="frontFade" x1="0" y1="0" x2="0" y2="1">
          <stop offset="0" stop-color="#ffffff"/><stop offset="1" stop-color="#e6e6e6"/>
        </linearGradient>
        <linearGradient id="skyTurf" x1="0" y1="0" x2="0" y2="1">
          <stop offset="0" stop-color="#2f7fd0"/><stop offset=".55" stop-color="#8cc4ee"/><stop offset=".6" stop-color="#5cb532"/><stop offset="1" stop-color="#3f9a22"/>
        </linearGradient>
        <linearGradient id="grassFade" x1="0" y1="0" x2="0" y2="1">
          <stop offset="0" stop-color="#e6e6e6"/><stop offset=".25" stop-color="#7cc243"/><stop offset="1" stop-color="#3d8f1f"/>
        </linearGradient>
      </defs>
      <rect class="panel-base" width="458" height="1098" fill="url(#frontFade)"/>
      <polygon class="top-band" points="0,0 458,0 458,70 0,285" fill="var(--red)"/>
      <g role="img" aria-label="Photo of a man riding a lawn mower on a green lawn under blue sky">
        <polygon points="0,300 430,100 458,118 458,470 165,640 0,590" fill="url(#skyTurf)"/>
      </g>
      <polygon class="accent-white" points="0,285 430,85 458,100 458,118 430,100 0,300" fill="var(--white)"/>
      <polyline class="accent-green" points="0,298 430,130 458,150" fill="none" stroke="var(--green)" stroke-width="6"/>
      <polyline class="chevron-line" points="0,600 165,650 458,478" fill="none" stroke="var(--ink)" stroke-width="9"/>
      <circle class="hole-ring" cx="229" cy="176" r="72" fill="var(--white)"/>
      <circle class="hole" cx="229" cy="176" r="62" fill="var(--ink)"/>

      <g transform="rotate(-22 220 560)" role="img" aria-label="Close-up photo of a mower wheel on grass">
        <rect x="148" y="492" width="140" height="140" fill="var(--red)"/>
        <rect x="156" y="500" width="124" height="124" fill="#5f8f3c"/>
      </g>
      <g transform="rotate(6 340 605)" role="img" aria-label="Photo of a man pushing a lawn mower in a backyard">
        <rect x="262" y="527" width="158" height="158" fill="var(--red)"/>
        <rect x="270" y="535" width="142" height="142" fill="#7dac47"/>
      </g>

      <text class="t-head" x="229" y="709" text-anchor="middle" font-size="24" fill="var(--red)">WE ARE IN</text>
      <text class="t-head" x="229" y="739" text-anchor="middle" font-size="24" fill="var(--ink)">YOUR NEIGHBORHOOD</text>
      <text class="t-head" x="229" y="769" text-anchor="middle" font-size="24" fill="var(--red)">EVERY TUESDAY!</text>

      <rect class="brand-band" x="0" y="793" width="458" height="50" fill="var(--green)"/>
      <polygon class="brand-plate" points="48,793 410,793 430,843 28,843" fill="var(--ink)"/>
      <text class="t-brand" x="229" y="831" text-anchor="middle" font-size="36" fill="var(--white)">VERDATURF</text>

      <text class="t-body" x="229" y="884" text-anchor="middle" font-size="16" fill="var(--red)">WE MOWED YOUR NEIGHBOR'S LAWN TODAY!</text>
      <line x1="72" y1="903" x2="390" y2="903" stroke="var(--ink)" stroke-width="2"/>
      <text class="t-bold" x="229" y="931" text-anchor="middle" font-size="18" fill="var(--ink)">CALL US TODAY! 512-748-3091</text>

      <g role="img" aria-label="Fresh green grass along the bottom edge">
        <rect x="0" y="945" width="458" height="153" fill="url(#grassFade)"/>
      </g>
      <rect class="coupon" x="58" y="1022" width="340" height="53" fill="none" stroke="var(--white)" stroke-width="2" stroke-dasharray="6 4"/>
      <text class="t-coupon" x="228" y="1060" text-anchor="middle" font-size="31" fill="var(--white)">10TH LAWN SERVICE FREE</text>
    </svg>
  </div>

  <!-- Back side -->
  <div class="hanger hanger--back">
    <svg viewBox="0 0 458 1098" xmlns="http://www.w3.org/2000/svg">
      <defs>
        <linearGradient id="backFade" x1="0" y1="0" x2="0" y2="1">
          <stop offset="0" stop-color="#e4e4e4"/><stop offset=".5" stop-color="#ffffff"/><stop offset="1" stop-color="#e6e6e6"/>
        </linearGradient>
        <linearGradient id="grassFade2" x1="0" y1="0" x2="0" y2="1">
          <stop offset="0" stop-color="#e6e6e6"/><stop offset=".25" stop-color="#7cc243"/><stop offset="1" stop-color="#3d8f1f"/>
        </linearGradient>
      </defs>
      <rect class="panel-base" width="458" height="1098" fill="url(#backFade)"/>
      <polygon class="top-band" points="0,0 458,0 458,240 170,110 55,62 0,100" fill="var(--green)"/>
      <polygon class="accent-grey" points="170,110 458,240 458,262 170,128" fill="#dcdcdc"/>
      <polygon class="hex-white" points="0,135 55,90 170,142 458,262 458,382 222,470 0,388" fill="var(--white)"/>
      <polyline class="chevron-top" points="0,135 55,90 170,142" fill="none" stroke="var(--ink)" stroke-width="8"/>
      <polyline class="chevron-red" points="0,388 222,472 458,382" fill="none" stroke="var(--red)" stroke-width="8"/>
      <polyline class="chevron-black" points="0,402 222,486 458,396" fill="none" stroke="var(--ink)" stroke-width="8"/>
      <circle class="hole-ring" cx="229" cy="176" r="72" fill="var(--white)"/>
      <circle class="hole" cx="229" cy="176" r="62" fill="var(--ink)"/>

      <text class="t-bold" x="229" y="317" text-anchor="middle" font-size="36" fill="var(--green-deep)">OUR LAWN SERVICE</text>
      <text class="t-bold" x="229" y="362" text-anchor="middle" font-size="36" fill="var(--red)">IS GUARANTEED</text>

      <g transform="rotate(-18 145 620)" role="img" aria-label="Photo of a lawn mower on green grass">
        <rect x="55" y="530" width="180" height="180" fill="var(--red)"/>
        <rect x="63" y="538" width="164" height="164" fill="#6e8f58"/>
      </g>
      <g transform="rotate(-20 320 610)" role="img" aria-label="Photo of a man starting a lawn mower on a lawn">
        <rect x="240" y="530" width="165" height="165" fill="var(--red)"/>
        <rect x="248" y="538" width="149" height="149" fill="#5f9a3a"/>
      </g>

      <rect class="brand-band" x="0" y="753" width="458" height="48" fill="var(--red)"/>
      <polygon class="brand-plate" points="48,753 408,753 430,801 28,801" fill="var(--ink)"/>
      <text class="t-brand" x="229" y="790" text-anchor="middle" font-size="36" fill="var(--white)">VERDATURF</text>

      <text class="t-bold" x="229" y="851" text-anchor="middle" font-size="22" fill="var(--red)">CALL US TODAY! 512-748-3091</text>
      <text class="t-body" x="229" y="879" text-anchor="middle" font-size="14.5" fill="var(--ink)">Get benefited by our services like quality time</text>
      <text class="t-body" x="229" y="897" text-anchor="middle" font-size="14.5" fill="var(--ink)">with their family, golf, sports, resting, etc., instead</text>
      <text class="t-body" x="229" y="915" text-anchor="middle" font-size="14.5" fill="var(--ink)">of mowing the lawn</text>

      <g role="img" aria-label="Fresh green grass along the bottom edge">
        <rect x="0" y="940" width="458" height="158" fill="url(#grassFade2)"/>
      </g>
      <rect class="coupon" x="58" y="1016" width="340" height="53" fill="none" stroke="var(--white)" stroke-width="2" stroke-dasharray="6 4"/>
      <text class="t-coupon" x="228" y="1054" text-anchor="middle" font-size="31" fill="var(--white)">10TH LAWN SERVICE FREE</text>
    </svg>
  </div>

</div>
</body>
</html>
```